Business Cards for Law Office of Miriam T. Haskell

I need a business card for my new estate planning law firm. I have attached my logo. I would like a design that is professional but not too formal or stuffy.

Target Market(s)

Professionals (lawyers, doctors, businesswomen) between the age of 30 and 50 who are tech-savvy and educated.

Industry/Entity Type

Lawyer

Contact Information for Business Card

Miriam T. Haskell

582 E. 67th Street
9th Floor
New York, NY 10065

Phone: (855) 407-6218
Direct: (917) 563-0472
Email: Miriam@MiriamTHaskellLaw.example
www.MiriamTHaskellLaw.example

Font styles to use
Other font styles liked:
• Corbel

Requirements
Must have
• On the front:
• Miriam T. Haskell, Esq.
• Owner & Founder
• 582 E. 67th Street
• 9th Floor
• New York, NY 10065
• Phone: (855) 407-6218
• Direct: (917) 563-0472
• Email: miriam@miriamthaskelllaw.example
• www.miriamthaskelllaw.example
• On the back:
• LOGO
Nice to have
• I want it to be professional but not too formal or stuffy. Please choose colors that go with my logo.
Should not have
• I don't want TOO MUCH color. Some color is good, but not too much.

```html
<!DOCTYPE html>
<html lang="en">
<head>
<meta charset="utf-8">
<title>Law Office of Miriam T. Haskell – Business Card</title>
<link rel="stylesheet" href="https://fonts.googleapis.com/css2?family=Questrial&display=swap">
<style>
  :root {
    --bg: #eef0f1;
    --paper: #fbfbfb;
    --orange: #e0782f;
    --purple: #8c1f8f;
    --ink: #2b2b2b;
    --text: #555659;
    --rule: #e0a070;
  }
  * { box-sizing: border-box; margin: 0; padding: 0; }
  html, body { width: 1200px; height: 800px; overflow: hidden; }
  body {
    background: var(--bg);
    font-family: "Questrial", "Trebuchet MS", sans-serif;
    display: flex;
    align-items: center;
    justify-content: center;
    gap: 40px;
  }
  .card {
    position: relative;
    width: 540px;
    height: 309px;
    background: var(--paper);
    box-shadow: 0 2px 10px rgba(0,0,0,0.12);
    overflow: hidden;
  }
  .card__accent {
    position: absolute;
    top: 0;
    right: 0;
    height: 100%;
    width: 96px;
    background: linear-gradient(90deg, var(--purple) 0, var(--orange) 18%, var(--orange) 100%);
  }

  /* Back: firm name */
  .brand-square {
    position: absolute;
    left: 22px;
    top: 168px;
    width: 26px;
    height: 24px;
    background: var(--purple);
  }
  .firm-name {
    position: absolute;
    left: 58px;
    top: 126px;
    width: 370px;
    text-align: center;
    padding: 12px 0;
    border-top: 1.5px solid var(--rule);
    border-bottom: 1.5px solid var(--rule);
    color: var(--purple);
    font-size: 18px;
    letter-spacing: 0.03em;
    text-transform: uppercase;
    white-space: nowrap;
  }

  /* Front: contact */
  .contact {
    position: absolute;
    left: 30px;
    top: 104px;
    list-style: none;
    color: var(--text);
    font-size: 12.5px;
    line-height: 1.3;
  }
  .contact__item {
    display: flex;
    align-items: center;
    gap: 12px;
    margin-bottom: 12px;
  }
  .contact__icon {
    flex: none;
    width: 26px;
    height: 26px;
    border-radius: 50%;
    background: var(--orange);
    display: flex;
    align-items: center;
    justify-content: center;
  }
  .contact__icon svg { width: 15px; height: 15px; fill: #fff; }
  .contact__name {
    color: var(--ink);
    font-weight: 700;
    text-transform: uppercase;
    font-size: 13px;
    letter-spacing: 0.02em;
  }
</style>
</head>
<body>

  <section class="card card--back">
    <div class="card__accent" role="img" aria-label="Orange and purple curved corner decoration"></div>
    <div class="brand-square"></div>
    <div class="firm-name">Law Office of Miriam T. Haskell</div>
  </section>

  <section class="card card--front">
    <div class="card__accent" role="img" aria-label="Orange and purple curved side decoration"></div>
    <ul class="contact">
      <li class="contact__item">
        <span class="contact__icon"><svg viewBox="0 0 16 16"><circle cx="8" cy="5" r="3.2"/><path d="M2 15c0-3.5 2.7-5.5 6-5.5s6 2 6 5.5z"/></svg></span>
        <span><span class="contact__name">Miriam T. Haskell, Esq.</span><br>Owner &amp; Founder</span>
      </li>
      <li class="contact__item">
        <span class="contact__icon"><svg viewBox="0 0 16 16"><path d="M4 1.5l2.4 3-1.4 1.7c.9 1.9 2.4 3.4 4.3 4.3l1.7-1.4 3 2.4-1.4 2.5C6.8 14 2 9.2 1.5 3z"/></svg></span>
        <span>Phone: (855) 407-6218<br>Direct: (917) 563-0472</span>
      </li>
      <li class="contact__item">
        <span class="contact__icon"><svg viewBox="0 0 16 16"><path d="M8 1a7 7 0 100 14A7 7 0 008 1zm0 1.6c.8 1 1.4 2.4 1.6 4H6.4C6.6 5 7.2 3.6 8 2.6zM2.7 8.8h2.3c.1 1.6.6 3 1.3 4.2A5.4 5.4 0 012.7 8.8zm0-1.6A5.4 5.4 0 016.3 3C5.6 4.2 5.1 5.6 5 7.2zM8 13.4c-.8-1-1.4-2.4-1.6-4.6h3.2c-.2 2.2-.8 3.6-1.6 4.6zm1.7-.4c.7-1.200 1.2-2.6 1.3-4.2h2.3a5.4 5.4 0 01-3.6 4.2zM11 7.2c-.1-1.6-.6-3-1.3-4.2a5.4 5.4 0 013.6 4.2z"/></svg></span>
        <span>miriam@miriamthaskelllaw.example<br>www.miriamthaskelllaw.example</span>
      </li>
      <li class="contact__item">
        <span class="contact__icon"><svg viewBox="0 0 16 16"><path d="M8 1.5L1 8h2v6.5h4v-4h2v4h4V8h2z"/></svg></span>
        <span>582 E. 67th Street<br>9th Floor<br>New York, NY 10065</span>
      </li>
    </ul>
  </section>

</body>
</html>
```